Brochure Design

Looking for designer to make a brochure (2 sided) similar to attached pdf. Will provide the details and graphics needed. PDF is similar style to what we want. PPT has new content.

```html
<!DOCTYPE html>
<html lang="en">
<head>
<meta charset="utf-8">
<title>Qelvora Brochure</title>
<link rel="stylesheet" href="https://fonts.googleapis.com/css2?family=Montserrat:ital,wght@0,400;0,600;0,700;1,300&family=Source+Sans+3:ital,wght@0,400;0,600;1,400&display=swap">
<style>
  :root {
    --backdrop: #f2bd3c;
    --accent: #e6d23a;
    --accent-deep: #c9b42a;
    --ink-dark: #1e1e20;
    --panel-top: #232325;
    --panel-bottom: #5c5c5e;
    --headline-grey: #8a8a8c;
    --body-light: #e4e4e4;
    --label-grey: #d9d9d9;
    --paper: #f7f7f7;
    --logo-grey: #4a4a4c;
  }
  * { box-sizing: border-box; margin: 0; padding: 0; }
  html, body { width: 1200px; height: 1200px; overflow: hidden; }
  body {
    background: var(--backdrop);
    font-family: "Source Sans 3", Arial, sans-serif;
    position: relative;
  }
  .page {
    position: absolute;
    top: 250px;
    width: 540px;
    height: 700px;
    overflow: hidden;
    background: linear-gradient(180deg, var(--panel-top) 0%, #2e2e30 45%, var(--panel-bottom) 88%, #8a8a8a 100%);
  }
  .page--front { left: 40px; }
  .page--back { left: 620px; }

  .footer-band {
    position: absolute; left: 0; right: 0; bottom: 0; height: 100px;
    background: var(--paper);
  }
  .footer-band--short { height: 70px; }
  .brand {
    position: absolute; bottom: 30px;
    display: flex; align-items: center; gap: 10px;
  }
  .brand__dot {
    width: 34px; height: 34px; border-radius: 50%;
    background: var(--logo-grey);
  }
  .brand__text { border-left: 1px solid var(--logo-grey); padding-left: 8px; }
  .brand__name {
    font-family: "Montserrat", sans-serif; font-weight: 600;
    font-size: 20px; color: var(--logo-grey); line-height: 1;
  }
  .brand__tagline {
    font-family: "Montserrat", sans-serif; font-weight: 400;
    font-size: 7.5px; letter-spacing: 0.5px; color: var(--logo-grey); margin-top: 3px;
  }
  .page--front .brand { left: 50px; }
  .page--back .brand { right: 40px; bottom: 18px; }

  /* Front page */
  .quote-mark { position: absolute; left: 38px; top: 30px; }
  .rule {
    position: absolute; left: 110px; right: 0; top: 42px;
    height: 1px; background: #6a6a6c;
  }
  .front-headline {
    position: absolute; left: 50px; top: 112px;
    font-family: "Montserrat", sans-serif; font-weight: 700;
    font-size: 17px; line-height: 1.15; color: var(--headline-grey);
  }
  .front-headline .highlight { color: var(--accent); }
  .front-copy {
    position: absolute; left: 50px; top: 190px; width: 245px;
    font-size: 9.4px; line-height: 1.45; color: var(--body-light);
  }
  .front-copy p { margin-bottom: 9px; }
  .front-copy .italic { font-style: italic; }
  .coverage-map {
    position: absolute; left: 300px; top: 80px;
    width: 440px; height: 440px; border-radius: 50%;
    background: radial-gradient(circle at 40% 45%, #8a7d5a 0%, #5c5a48 35%, #3d4a3a 60%, #2d2c44 100%);
  }
  .callout {
    position: absolute; white-space: nowrap;
    font-family: "Montserrat", sans-serif; font-weight: 600;
    font-size: 10px; line-height: 1.1; text-align: center;
    color: var(--ink-dark); padding: 6px 10px;
  }
  .callout--grey { background: var(--label-grey); }
  .callout--yellow { background: var(--accent-deep); }
  .pin { position: absolute; }
  .coverage-note {
    position: absolute; right: 30px; top: 540px; text-align: right;
    font-family: "Montserrat", sans-serif; font-size: 7px; letter-spacing: 1.5px;
    text-transform: uppercase; color: var(--accent); line-height: 1.5;
  }

  /* Back page */
  .aerial-view {
    position: absolute; left: 0; top: 0; width: 540px; height: 300px;
    background: linear-gradient(180deg, #2b2b36 0%, #6b6450 18%, #cfc6ad 34%, #8e9a6a 50%, #8a8d88 62%, #55704a 80%, #3b4f35 100%);
  }
  .hero-pin { position: absolute; left: 350px; top: 225px; }
  .pin-photo {
    position: absolute; left: 378px; top: 256px;
    width: 100px; height: 120px; border-radius: 50%;
    background: linear-gradient(160deg, #8a9ab0 0%, #5a6680 45%, #2a3050 100%);
  }
  .pin-shadow { position: absolute; left: 330px; top: 470px; }
  .back-headline {
    position: absolute; left: 45px; top: 365px; width: 300px;
    font-family: "Montserrat", sans-serif; font-weight: 700;
    font-size: 21px; line-height: 1.15; color: #6e6e70;
  }
  .back-subhead {
    position: absolute; left: 45px; top: 448px;
    font-family: "Montserrat", sans-serif; font-style: italic; font-weight: 300;
    font-size: 19px; color: var(--accent);
  }
  .back-copy {
    position: absolute; left: 45px; top: 484px; width: 270px;
    font-size: 9.4px; line-height: 1.45; color: var(--body-light);
  }
</style>
</head>
<body>

<section class="page page--front">
  <svg class="quote-mark" width="64" height="52" viewBox="0 0 64 52" aria-hidden="true">
    <path d="M4 0h14v30a10 10 0 1 1-14 9z M34 0h14v30a10 10 0 1 1-14 9z" fill="var(--accent-deep)"/>
  </svg>
  <div class="rule"></div>

  <h1 class="front-headline">
    Explore Potential.<br>
    Expand Possibilities.<br>
    <span class="highlight">Experience Qelvora.</span>
  </h1>

  <div class="front-copy">
    <p>Discover the power of geography with Qelvora, where we transform dynamic geospatial data into compelling narratives about places and their potential futures. Geography is more than just maps—it's a vibrant story unfolding in real-time, revealing not just the present state of an area but predicting what comes next. At Qelvora, we are your guide to this story, providing easy access to an extensive range of geospatial data and unique datasets that empower your organization with crucial insights and intelligence.</p>
    <p class="italic">Our industry-leading mobile platform, Orvalix, is just the beginning. We've developed advanced algorithms that can predict patterns and movements, helping you anticipate and respond to future events with precision. Whether you're looking to optimize logistics, enhance market penetration, or monitor environmental changes, Orvalix offers the clarity and foresight you need to make informed decisions.</p>
    <p>Introducing Spotryn, our latest innovation in image location detection. This cutting-edge tool further expands your capabilities to decode the geography of any area, uncover hidden stories, and tap into unseen opportunities. At Qelvora, we're committed to equipping you with the tools to tackle your most complex challenges. Let us help you navigate the geographical narratives of tomorrow, today.</p>
  </div>

  <div class="coverage-map" role="img" aria-label="Aerial view of a beach and parking area overlaid with coloured dots marking detected devices"></div>

  <svg class="pin" style="left:415px;top:345px" width="22" height="30" viewBox="0 0 22 30" aria-hidden="true">
    <path d="M11 0a11 11 0 0 1 11 11c0 8-11 19-11 19S0 19 0 11A11 11 0 0 1 11 0z" fill="var(--accent-deep)"/>
    <circle cx="11" cy="11" r="4" fill="var(--ink-dark)"/>
  </svg>
  <div class="callout callout--grey" style="left:385px;top:385px">Predicted Location</div>

  <svg class="pin" style="left:345px;top:443px" width="14" height="19" viewBox="0 0 22 30" aria-hidden="true">
    <path d="M11 0a11 11 0 0 1 11 11c0 8-11 19-11 19S0 19 0 11A11 11 0 0 1 11 0z" fill="var(--accent-deep)"/>
    <circle cx="11" cy="11" r="4" fill="var(--ink-dark)"/>
  </svg>
  <div class="callout callout--grey" style="left:315px;top:472px">Actual Location<br>of Photo</div>

  <div class="coverage-note">*Actual devices detected<br>in the vicinity.</div>

  <div class="footer-band"></div>
  <div class="brand">
    <div class="brand__dot"></div>
    <div class="brand__text">
      <div class="brand__name">Qelvora</div>
      <div class="brand__tagline">Geospatial Intelligence</div>
    </div>
  </div>
</section>

<section class="page page--back">
  <div class="aerial-view" role="img" aria-label="Aerial photo of a coastal road, beach and parking lots"></div>

  <svg class="pin" style="left:445px;top:118px" width="18" height="24" viewBox="0 0 22 30" aria-hidden="true">
    <path d="M11 0a11 11 0 0 1 11 11c0 8-11 19-11 19S0 19 0 11A11 11 0 0 1 11 0z" fill="var(--accent-deep)"/>
    <circle cx="11" cy="11" r="4" fill="var(--ink-dark)"/>
  </svg>
  <div class="callout callout--yellow" style="left:395px;top:148px">Predicted Location</div>

  <svg class="pin" style="left:175px;top:218px" width="18" height="24" viewBox="0 0 22 30" aria-hidden="true">
    <path d="M11 0a11 11 0 0 1 11 11c0 8-11 19-11 19S0 19 0 11A11 11 0 0 1 11 0z" fill="var(--accent-deep)"/>
    <circle cx="11" cy="11" r="4" fill="var(--ink-dark)"/>
  </svg>
  <div class="callout callout--yellow" style="left:135px;top:248px">Actual Location<br>of Photo</div>

  <svg class="pin-shadow" width="200" height="70" viewBox="0 0 200 70" aria-hidden="true">
    <ellipse cx="100" cy="35" rx="100" ry="35" fill="#4a4a4c" opacity="0.6"/>
  </svg>
  <svg class="hero-pin" width="156" height="270" viewBox="0 0 156 270" aria-hidden="true">
    <path d="M78 0C35 0 0 36 0 84c0 62 78 186 78 186S156 146 156 84C156 36 121 0 78 0z" fill="var(--accent-deep)"/>
  </svg>
  <div class="pin-photo" role="img" aria-label="Street photo of a parked car near a lighthouse"></div>

  <h2 class="back-headline">Instantly pinpoint<br>the location of any<br>photo or video</h2>
  <div class="back-subhead">—no metadata required!</div>

  <p class="back-copy">Powered by multiple cutting-edge AI algorithms, Qelvora's image location detection tool rapidly pinpoints the location of your photos and videos. It meticulously analyzes distinguishable landmarks, rock formations, vegetation, and various unique identifiers. Even when faced with altered or no metadata, our AI leverages visual analysis to accurately determine the actual location of your image. The more detailed or famous the location, the higher the precision of our results. Additionally, our system continuously learns and refines its accuracy with every use, guaranteeing progressively better outcomes.</p>

  <div class="footer-band footer-band--short"></div>
  <div class="brand">
    <div class="brand__dot"></div>
    <div class="brand__text">
      <div class="brand__name">Qelvora</div>
      <div class="brand__tagline">Geospatial Intelligence</div>
    </div>
  </div>
</section>

</body>
</html>
```